Business Card Design

Hoping for a black background business card, minimalistic design.
With the Marble Crest logo you created in white.

I would like to include:
My Name and title
Address (street address)
Reception: (phone number)
Fax: (fax number)
Reception: (email address)
Direct email: (email address)
Instagram: (ig handle)

```html
<!DOCTYPE html>
<html lang="en">
<head>
<meta charset="utf-8">
<title>Marble Crest — Business Card</title>
<link rel="stylesheet" href="https://fonts.googleapis.com/css2?family=Oswald:wght@300;400;600&display=swap">
<style>
  :root {
    --bg: #c9c9c9;
    --card-light: #f6f6f4;
    --card-dark: #0b0b0b;
    --ink: #111111;
    --ink-soft: #555555;
    --paper-white: #ffffff;
  }
  html, body {
    margin: 0;
    padding: 0;
    width: 1200px;
    height: 876px;
    overflow: hidden;
    background: var(--bg);
  }
  .canvas {
    position: relative;
    width: 1200px;
    height: 876px;
    background: radial-gradient(ellipse at 50% 35%, #e2e2e2 0%, var(--bg) 75%);
    font-family: "Oswald", "Arial Narrow", sans-serif;
  }
  .card {
    position: absolute;
    width: 520px;
    height: 298px;
    box-sizing: border-box;
    box-shadow: 0 8px 22px rgba(0,0,0,0.22);
  }
  .card--back {
    left: 50px;
    top: 330px;
    background: var(--card-light);
    color: var(--ink);
  }
  .card--front {
    left: 630px;
    top: 250px;
    background: radial-gradient(ellipse at 40% 40%, #1c1c1c 0%, var(--card-dark) 70%);
    color: var(--paper-white);
    display: flex;
    align-items: center;
    justify-content: center;
  }
  .brand {
    display: flex;
    align-items: center;
    gap: 12px;
  }
  .brand__dot {
    border-radius: 50%;
    border: 3px solid currentColor;
    box-sizing: border-box;
  }
  .brand__name {
    font-weight: 400;
    letter-spacing: 0.14em;
    text-transform: uppercase;
    white-space: nowrap;
  }
  .card--front .brand__dot { width: 52px; height: 52px; }
  .card--front .brand__name { font-size: 30px; }
  .card--back .brand {
    position: absolute;
    right: 34px;
    top: 128px;
  }
  .card--back .brand__dot { width: 34px; height: 34px; border-width: 2px; }
  .card--back .brand__name { font-size: 19px; }
  .person {
    position: absolute;
    left: 34px;
    top: 30px;
  }
  .person__name {
    margin: 0;
    font-size: 26px;
    font-weight: 600;
    letter-spacing: 0.01em;
    line-height: 1;
  }
  .person__title {
    margin: 6px 0 0 0;
    font-size: 12px;
    font-weight: 300;
    color: var(--ink-soft);
    letter-spacing: 0.06em;
  }
  .contact {
    list-style: none;
    margin: 0;
    padding: 0;
    font-size: 11.5px;
    font-weight: 600;
    line-height: 1.35;
    text-transform: uppercase;
  }
  .contact--personal {
    position: absolute;
    left: 34px;
    top: 112px;
  }
  .contact--office {
    position: absolute;
    left: 270px;
    bottom: 26px;
  }
</style>
</head>
<body>
<main class="canvas">
  <section class="card card--back" aria-label="Card back with contact details">
    <header class="person">
      <h1 class="person__name">FULL NAME</h1>
      <p class="person__title">TITLE</p>
    </header>
    <ul class="contact contact--personal">
      <li>Address: (Street Address)</li>
      <li>Direct Email: (Email Address)</li>
      <li>Instagram: (IG Handle)</li>
    </ul>
    <div class="brand">
      <span class="brand__dot"></span>
      <span class="brand__name">Marble Crest</span>
    </div>
    <ul class="contact contact--office">
      <li>Reception: (Phone Number)</li>
      <li>Fax: (Fax Number)</li>
      <li>Reception: (Email Address)</li>
    </ul>
  </section>

  <section class="card card--front" aria-label="Card front with brand name">
    <div class="brand">
      <span class="brand__dot"></span>
      <span class="brand__name">Marble Crest</span>
    </div>
  </section>
</main>
</body>
</html>
```